Harvest Gathering event flyer

I would like a church event flyer designed. The event is called "HARVEST GATHERING 2018". I am looking for a professional, yet catchy design that uses our brand colors and logo creatively while communicating key information of the event effectively.

1. The logo is attached in two color formats. The designer has the choice to use them as he/she want.

2. The location of the event is: Lindqvist Community Center, 482 Tamsworth Street, Portland, ME 04102
3. Time and date of event. The designer can organize and format the date and time as he/she pleases.
December 28th, 29th @ 7:00PM
December 30th @ 10:00AM
4. The topic of the event is "Tongues of fire". The designer is free to use this phrase as he/she pleases to create a good composition.
5. Speaker: Prophet Marcus Obuya
6. Contact information: contact@cedarbrookfellowship.org - Telephone number: 207 555 0148

7. I would also like the following three words on the flyer. These words describe the focus of the event: FIRE, REVIVAL, PROPHETIC

```html
<!DOCTYPE html>
<html lang="en">
<head>
<meta charset="utf-8">
<title>Harvest Gathering 2018 – Flyer</title>
<link href="https://fonts.googleapis.com/css2?family=Oswald:wght@600;700&family=Montserrat:wght@400;500;600;700&display=swap" rel="stylesheet">
<style>
  :root{
    --navy:#0d3461;
    --orange:#f39a1e;
    --ink:#1c1c1c;
    --paper:#ffffff;
    --cream:#f2eee6;
    --backdrop:#e6e6e6;
  }
  *{box-sizing:border-box;margin:0;padding:0}
  html,body{width:1200px;height:1200px;overflow:hidden;background:var(--backdrop)}
  .flyer{
    position:absolute;left:211px;top:50px;width:778px;height:1100px;
    background:var(--paper);overflow:hidden;
    font-family:"Montserrat",sans-serif;color:var(--ink);
    box-shadow:0 6px 24px rgba(0,0,0,.15);
  }
  .cream-panel{position:absolute;left:370px;top:0;width:408px;height:420px;background:var(--cream)}
  .portrait-frame{
    position:absolute;left:365px;top:-100px;width:500px;height:500px;border-radius:50%;
    border:12px solid var(--orange);overflow:hidden;background:var(--orange);
  }
  .portrait{
    width:100%;height:100%;border-radius:50%;
    background:radial-gradient(circle at 40% 45%,#6b4a35 0 22%,#23232a 40%,#1a1d26 70%,#c9d6e6 100%);
  }
  .brand{position:absolute;left:50px;top:62px;display:flex;align-items:center;gap:12px}
  .brand-dot{width:24px;height:24px;border-radius:50%;background:var(--orange)}
  .brand-name{font-family:"Montserrat",sans-serif;font-weight:700;font-size:34px;letter-spacing:3px;color:var(--navy)}
  .event-title{position:absolute;left:50px;top:140px;font-family:"Oswald",sans-serif;font-weight:700;font-size:52px;line-height:1.08;text-transform:uppercase}
  .event-title .orange{color:var(--orange)}
  .event-title .navy{color:var(--navy)}
  .topic{position:absolute;left:50px;top:370px;font-family:"Oswald",sans-serif;font-weight:700;font-size:32px;color:var(--navy);text-transform:uppercase}
  .focus-list{position:absolute;left:62px;top:424px;list-style:none}
  .focus-list li{display:flex;align-items:center;gap:14px;height:38px;font-family:"Oswald",sans-serif;font-weight:600;font-size:18px;color:var(--navy);text-transform:uppercase}
  .focus-list li:nth-child(2){margin-left:28px}
  .focus-list li:nth-child(3){margin-left:56px}
  .focus-icon{width:28px;height:28px}
  .speaker-pill{
    position:absolute;left:40px;top:560px;width:738px;height:50px;background:var(--navy);
    border-radius:25px 0 0 25px;color:#fff;font-size:20px;font-weight:500;
    display:flex;align-items:center;padding-left:34px;letter-spacing:.5px;
  }
  .info-row{position:absolute;left:50px;display:flex;align-items:center;gap:30px}
  .info-row.schedule{top:650px}
  .info-row.venue{top:810px}
  .info-badge{width:84px;height:84px;border-radius:50%;background:#fff;border:3px solid var(--orange);box-shadow:0 4px 10px rgba(0,0,0,.18);display:flex;align-items:center;justify-content:center;flex:none}
  .schedule-lines p{font-size:33px;font-weight:500;line-height:1.4;color:var(--ink)}
  .venue-name{font-size:30px;font-weight:600;color:var(--orange);text-transform:uppercase;line-height:1.2}
  .venue-address{font-size:23px;font-weight:600;color:var(--ink);margin-top:4px}
  .contact-band{
    position:absolute;left:0;bottom:0;width:100%;height:90px;background:var(--navy);
    display:flex;align-items:center;justify-content:space-around;color:#fff;font-size:18px;font-weight:500;
  }
  .contact-item{display:flex;align-items:center;gap:10px}
</style>
</head>
<body>
<main class="flyer">
  <div class="cream-panel"></div>
  <div class="portrait-frame"><div class="portrait" role="img" aria-label="Portrait photo of the speaker, Prophet Marcus Obuya, smiling in glasses and a dark suit"></div></div>

  <div class="brand"><span class="brand-dot"></span><span class="brand-name">ASHVALE</span></div>

  <h1 class="event-title"><span class="orange">Harvest</span><br><span class="navy">Gathering</span><br><span class="orange">2018</span></h1>

  <h2 class="topic">Tongues of Fire</h2>
  <ul class="focus-list">
    <li><svg class="focus-icon" viewBox="0 0 28 28"><circle cx="14" cy="14" r="12.5" fill="none" stroke="#f39a1e" stroke-width="1.5"/><path d="M14 7c1 4 5 5 5 10a5 5 0 0 1-10 0c0-3 2-4 2-6 1 1 2 2 2 3 1-2 1-4 1-7z" fill="#f39a1e"/></svg>Fire</li>
    <li><svg class="focus-icon" viewBox="0 0 28 28"><circle cx="14" cy="14" r="12.5" fill="none" stroke="#f39a1e" stroke-width="1.5"/><path d="M14 7l5 7-5 7-5-7z" fill="none" stroke="#f39a1e" stroke-width="1.5"/></svg>Revival</li>
    <li><svg class="focus-icon" viewBox="0 0 28 28"><circle cx="14" cy="14" r="12.5" fill="none" stroke="#f39a1e" stroke-width="1.5"/><circle cx="14" cy="15" r="5" fill="#f39a1e"/></svg>Prophetic</li>
  </ul>

  <div class="speaker-pill">SPEAKER: Prophet Marcus Obuya</div>

  <section class="info-row schedule">
    <div class="info-badge"><svg width="44" height="44" viewBox="0 0 44 44"><rect x="4" y="8" width="30" height="28" rx="3" fill="none" stroke="#0d3461" stroke-width="2.5"/><line x1="4" y1="16" x2="34" y2="16" stroke="#0d3461" stroke-width="2.5"/><line x1="11" y1="4" x2="11" y2="11" stroke="#0d3461" stroke-width="2.5"/><line x1="27" y1="4" x2="27" y2="11" stroke="#0d3461" stroke-width="2.5"/><circle cx="33" cy="32" r="8" fill="#fff" stroke="#0d3461" stroke-width="2.5"/><path d="M33 28v4h3" fill="none" stroke="#0d3461" stroke-width="2"/></svg></div>
    <div class="schedule-lines">
      <p>December 28th, 29th @ 7:00PM</p>
      <p>December 30th @ 10:00AM</p>
    </div>
  </section>

  <section class="info-row venue">
    <div class="info-badge"><svg width="40" height="44" viewBox="0 0 40 44"><path d="M20 4a11 11 0 0 1 11 11c0 8-11 19-11 19S9 23 9 15A11 11 0 0 1 20 4z" fill="none" stroke="#0d3461" stroke-width="2.5"/><circle cx="20" cy="15" r="4" fill="#0d3461"/><path d="M8 36c4 4 20 4 24 0" fill="none" stroke="#f39a1e" stroke-width="2"/></svg></div>
    <div>
      <p class="venue-name">Lindqvist Community Center</p>
      <p class="venue-address">482 Tamsworth Street, Portland, ME 04102</p>
    </div>
  </section>

  <footer class="contact-band">
    <span class="contact-item"><svg width="20" height="20" viewBox="0 0 20 20"><path d="M4 2l4 1 1 4-2 2a11 11 0 0 0 4 4l2-2 4 1 1 4-2 2C8 18 2 12 2 4z" fill="#f39a1e"/></svg>207 555 0148</span>
    <span class="contact-item"><svg width="20" height="16" viewBox="0 0 20 16"><rect x="1" y="1" width="18" height="14" fill="none" stroke="#f39a1e" stroke-width="2"/><path d="M1 1l9 7 9-7" fill="none" stroke="#f39a1e" stroke-width="2"/></svg>contact@cedarbrookfellowship.org</span>
    <span class="contact-item"><svg width="20" height="20" viewBox="0 0 20 20"><circle cx="10" cy="10" r="8" fill="none" stroke="#f39a1e" stroke-width="2"/><ellipse cx="10" cy="10" rx="3.5" ry="8" fill="none" stroke="#f39a1e" stroke-width="1.5"/><line x1="2" y1="10" x2="18" y2="10" stroke="#f39a1e" stroke-width="1.5"/></svg>www.ashvale.org</span>
  </footer>
</main>
</body>
</html>
```